Silver Creek Plumbing Business card & letter head design

We need a new business card and letter head for our plumbing company called silver creek plumbing. attached is the companys logo. We provide domestic and commercial plumbing services in regional western Australia. We are after Something simple yet nice to look at and something that fits within the trade industry.

Target Market(s)

trade/building industry

Contact Information for Business Card

Darl Hensby
Manager
0461 238 574
enquiries@scplumbwork.net.au
ABN: 47 381 905 462
PCL: 5187

Domestic & Commercial Plumbing
Tip Truck & Excavator hire

Colors

Designer to choose colors to be used in the design.

```html
<!DOCTYPE html>
<html lang="en">
<head>
<meta charset="utf-8">
<title>Silver Creek Plumbing – Stationery</title>
<link rel="stylesheet" href="https://fonts.googleapis.com/css2?family=Lato:wght@400;700&family=Oswald:wght@500&display=swap">
<style>
  :root{
    --bg:#c6c6c6;
    --paper:#ffffff;
    --blue:#1159a8;
    --grey:#58585a;
    --text:#444446;
    --card-grey:#5a5a5c;
    --card-blue:#0d5aa7;
  }
  *{margin:0;padding:0;box-sizing:border-box}
  html,body{width:1200px;height:1200px;overflow:hidden;background:var(--bg);font-family:"Lato",sans-serif}
  .canvas{position:relative;width:1200px;height:1200px}

  .letterhead{position:absolute;left:32px;top:95px;width:784px;height:1009px;background:var(--paper);box-shadow:0 2px 6px rgba(0,0,0,.25)}
  .brand{position:absolute;font-family:"Lato",sans-serif;font-weight:700;color:var(--blue);text-align:center;line-height:1.05;text-transform:uppercase}
  .letterhead .brand{left:66px;top:66px;width:245px;font-size:34px}
  .letterhead .contact{position:absolute;left:485px;top:68px;border-left:2px solid var(--blue);padding-left:19px;font-size:18.6px;line-height:24.6px;color:var(--text)}
  .label{color:var(--blue);font-weight:700}

  .card{position:absolute;left:851px;width:316px;height:182px;background:var(--paper);box-shadow:0 2px 5px rgba(0,0,0,.25)}
  .card .brand{left:0;right:0;font-size:22px}
  .card--grey{background:var(--card-grey)}
  .card--blue{background:var(--card-blue)}
  .card--grey .brand,.card--blue .brand{color:#fff}

  .person{position:absolute;left:0;width:316px;display:flex}
  .person .id{width:155px;padding-right:12px;text-align:right}
  .person .name{font-family:"Oswald",sans-serif;font-weight:500;font-size:22px;line-height:24px;color:var(--blue);text-transform:uppercase;letter-spacing:-.2px}
  .person .role{font-size:7.5px;color:var(--text);margin-top:1px}
  .person .details{border-left:1px solid var(--blue);padding-left:11px;font-size:7.5px;line-height:11.5px;color:var(--text)}

  .tagline{position:absolute;left:0;right:0;text-align:center;font-size:7.8px;font-weight:700;color:var(--text)}
  .card--grey .tagline,.card--blue .tagline{color:#fff}
  .tagline .sep{margin:0 5px}
</style>
</head>
<body>
<main class="canvas">

  <section class="letterhead">
    <div class="brand">Silver Creek<br>Plumbing</div>
    <div class="contact">
      <div>0461 238 574</div>
      <div>enquiries@scplumbwork.net.au</div>
      <div><span class="label">ABN:</span> 47 381 905 462</div>
      <div><span class="label">PCL:</span> 5187</div>
    </div>
  </section>

  <section class="card" style="top:95px">
    <div class="brand" style="top:30px">Silver Creek<br>Plumbing</div>
    <div class="person" style="top:118px">
      <div class="id"><div class="name">Darl Hensby</div><div class="role">Manager</div></div>
      <div class="details">
        <div>0461 238 574</div>
        <div>enquiries@scplumbwork.net.au</div>
        <div><span class="label">ABN:</span> 47 381 905 462</div>
        <div><span class="label">PCL:</span> 5187</div>
      </div>
    </div>
  </section>

  <section class="card" style="top:302px">
    <div class="person" style="top:73px">
      <div class="id"><div class="name">Darl Hensby</div><div class="role">Manager</div></div>
      <div class="details">
        <div>0461 238 574</div>
        <div>enquiries@scplumbwork.net.au</div>
        <div><span class="label">ABN:</span> 47 381 905 462</div>
        <div><span class="label">PCL:</span> 5187</div>
      </div>
    </div>
  </section>

  <section class="card" style="top:510px">
    <div class="brand" style="top:66px">Silver Creek<br>Plumbing</div>
    <div class="tagline" style="top:159px">Domestic &amp; Commercial Plumbing<span class="sep">|</span>Tip Truck &amp; Excavator hire</div>
  </section>

  <section class="card card--grey" style="top:717px">
    <div class="brand" style="top:66px">Silver Creek<br>Plumbing</div>
    <div class="tagline" style="top:159px">Domestic &amp; Commercial Plumbing<span class="sep">|</span>Tip Truck &amp; Excavator hire</div>
  </section>

  <section class="card card--blue" style="top:925px">
    <div class="brand" style="top:66px">Silver Creek<br>Plumbing</div>
    <div class="tagline" style="top:159px">Domestic &amp; Commercial Plumbing<span class="sep">|</span>Tip Truck &amp; Excavator hire</div>
  </section>

</main>
</body>
</html>
```